Business card Pfotenweide

Business card is for a self-employed dog trainer with own dog school. Name and logo of the dog school are available. Color specifications as well. The design should be classy and minimalist, but also modern. An already existing idea would be: Front: Only the logo Back: Contact data

Font styles to use
Serif
Sans Serif
Other font styles liked:
• Trajan Pro

Colors
f78f20

Requirements
Must have
• Name: Marlene Kessel-Brand Title: Dipl. Dog Trainer Contain my logo Follow my font and color preferences (see files)

```html
<!DOCTYPE html>
<html lang="de">
<head>
<meta charset="utf-8">
<title>Pfotenweide – Visitenkarte</title>
<link rel="stylesheet" href="https://fonts.googleapis.com/css2?family=Cinzel:wght@400;500&family=Roboto:wght@300;400&display=swap">
<style>
  :root {
    --stage: #2b2b2d;
    --taupe: #7e6c5f;
    --taupe-light: #8c7a6c;
    --paper: #ffffff;
    --ink: #7a6759;
    --ink-soft: #5e5e5e;
    --rule: #8a7868;
  }
  * { box-sizing: border-box; margin: 0; padding: 0; }
  html, body { width: 1200px; height: 900px; overflow: hidden; }
  body {
    background: var(--stage);
    position: relative;
    font-family: "Roboto", Arial, sans-serif;
  }
  .card {
    position: absolute;
    width: 620px;
    height: 354px;
    border-radius: 22px;
    box-shadow: 0 12px 30px rgba(0,0,0,.45);
  }
  .card--front {
    left: 170px; top: 60px;
    background: linear-gradient(135deg, var(--taupe-light), var(--taupe));
    display: flex; flex-direction: column; align-items: center; justify-content: center;
  }
  .card--back {
    left: 410px; top: 480px;
    background: var(--paper);
  }
  .brand-mark {
    border-radius: 50%;
    display: block;
  }
  .card--front .brand-mark { width: 150px; height: 150px; background: var(--paper); }
  .card--front .brand-name {
    margin-top: 18px;
    font-family: "Cinzel", "Times New Roman", serif;
    font-size: 34px; letter-spacing: 2px;
    color: var(--paper);
  }
  .card--back .brand {
    position: absolute; left: 48px; top: 42px;
    display: flex; flex-direction: column; align-items: center;
  }
  .card--back .brand-mark { width: 130px; height: 130px; background: var(--taupe); }
  .card--back .brand-name {
    margin-top: 14px;
    font-family: "Cinzel", "Times New Roman", serif;
    font-size: 28px; letter-spacing: 2px;
    color: var(--ink);
  }
  .divider {
    position: absolute; left: 150px; top: 232px;
    width: 300px; height: 1px; background: var(--rule);
  }
  .person {
    position: absolute; right: 40px; top: 40px; text-align: right;
  }
  .person-name {
    font-family: "Cinzel", "Times New Roman", serif;
    font-size: 21px; color: var(--ink); letter-spacing: .5px;
  }
  .person-title {
    font-size: 18px; font-weight: 300; color: var(--ink-soft); margin-top: 2px;
  }
  .address {
    margin-top: 22px;
    font-style: normal; font-size: 15px; font-weight: 300; line-height: 1.4;
    color: var(--ink-soft);
  }
  .contact {
    position: absolute; left: 150px; top: 252px;
    list-style: none;
    font-size: 16px; font-weight: 300; color: var(--ink-soft);
  }
  .contact li { display: flex; align-items: center; gap: 12px; line-height: 26px; }
  .contact svg { width: 14px; height: 14px; fill: none; stroke: var(--ink-soft); stroke-width: 1.4; }
</style>
</head>
<body>
  <section class="card card--front" aria-label="Vorderseite">
    <span class="brand-mark" aria-hidden="true"></span>
    <span class="brand-name">PFOTENWEIDE</span>
  </section>

  <section class="card card--back" aria-label="Rückseite">
    <div class="brand">
      <span class="brand-mark" aria-hidden="true"></span>
      <span class="brand-name">PFOTENWEIDE</span>
    </div>

    <div class="person">
      <p class="person-name">Marlene Kessel-Brand</p>
      <p class="person-title">Dipl. Hundetrainerin</p>
      <address class="address">
        Unit 8, The Linden Court,<br>
        Mill Lane, Harwick,<br>
        Herts HW4 2LP
      </address>
    </div>

    <span class="divider" aria-hidden="true"></span>

    <ul class="contact">
      <li>
        <svg viewBox="0 0 14 14" aria-hidden="true"><rect x="3.5" y="1" width="7" height="12" rx="1.2"/><line x1="6" y1="11" x2="8" y2="11"/></svg>
        +41 79 482 5613
      </li>
      <li>
        <svg viewBox="0 0 14 14" aria-hidden="true"><rect x="1" y="3" width="12" height="8.5" rx="1"/><polyline points="1,3.5 7,8 13,3.5"/></svg>
        hallo@pfotenweide.ch
      </li>
      <li>
        <svg viewBox="0 0 14 14" aria-hidden="true"><circle cx="7" cy="7" r="6"/><ellipse cx="7" cy="7" rx="2.6" ry="6"/><line x1="1" y1="7" x2="13" y2="7"/></svg>
        www.pfotenweide.ch
      </li>
    </ul>
  </section>
</body>
</html>
```